Wordpress Design Project

I need a wordpress design for a new business called the Skyvale Personal Development Center. We offer online and live self improvement programs and seminars that utilize self hypnosis.. I have a logo that I want the design built around, file is attached (I don't have a problem with you moving the logo words around, I just want to keep same design, font, colors)

The completed project will be the design and code for a child theme for the meridian framework. This will include the home page design and 3 separate subpage variation designs based on the main theme.

The design should communicate growth, potential and success.

Target Market(s)

70% women, well educated, open to alternative

Industry/Entity Type

Business

Requirements
Must have
• A key part of this design is having an effective optin box located on the right side. The main goal of this site is to get people to optin to my email list followed by easy navigation to different programs and content that are on the site.

```html
<!DOCTYPE html>
<html lang="en">
<head>
<meta charset="utf-8">
<title>Skyvale Personal Development Center</title>
<link rel="stylesheet" href="https://fonts.googleapis.com/css2?family=Cabin:wght@400;500;600;700&family=Arimo:wght@400;700&display=swap">
<style>
:root{
  --purple:#8b3c9c;
  --indigo:#2d2d8c;
  --indigo-dark:#24247a;
  --text:#6a6a6a;
  --nav:#5a5a5a;
  --rule:#e2e2e2;
  --header-bg:#f3f3f3;
  --white:#ffffff;
}
*{margin:0;padding:0;box-sizing:border-box}
html,body{width:1200px;height:1031px;overflow:hidden;background:var(--white)}
body{position:relative;font-family:"Arimo",Arial,sans-serif;color:var(--text);font-size:11.3px}
.abs{position:absolute}
.top-strip{left:0;top:0;width:1200px;height:7px;background:var(--purple)}
.site-header{left:0;top:7px;width:1200px;height:125px;background:linear-gradient(90deg,#ececec,#f7f7f7 30%,#f4f4f4 70%,#ebebeb)}
.brand{left:152px;top:42px;display:flex;align-items:center;gap:8px}
.brand-mark{width:58px;height:58px;border-radius:50%;background:var(--indigo)}
.brand-name{font-family:"Cabin",sans-serif;font-weight:600;color:var(--indigo);line-height:1.05;font-size:11px;letter-spacing:.3px}
.brand-name .big{display:block;font-size:26px;letter-spacing:0}
.main-nav{top:65px;left:0;font-family:"Cabin",sans-serif;font-weight:600;font-size:11.6px;color:var(--nav)}
.main-nav a{position:absolute;color:inherit;text-decoration:none;white-space:nowrap;transform:translateX(-50%)}
.main-nav a.active{color:var(--indigo)}
.nav-underline{left:486px;top:86px;width:51px;height:3px;background:var(--indigo)}
.nav-pointer{left:508px;top:82px;width:0;height:0;border-left:4px solid transparent;border-right:4px solid transparent;border-bottom:4px solid var(--indigo)}
.hero-band{left:0;top:132px;width:1200px;height:350px;background:var(--indigo)}
.slider-frame{left:150px;top:148px;width:900px;height:358px;background:var(--white)}
.slider-shadow{left:185px;top:500px;width:830px;height:16px;border-radius:50%;background:radial-gradient(ellipse at center,rgba(0,0,0,.12),rgba(0,0,0,0) 70%)}
.slide{left:157px;top:155px;width:886px;height:342px;background:linear-gradient(100deg,#e8ecf4 0%,#cfd9ea 35%,#a9cbe8 65%,#41a6dc 85%,#7cc4ea 100%)}
.slide-dots{left:964px;top:465px;display:flex;gap:3.5px}
.slide-dots span{width:16px;height:16px;border-radius:50%;background:var(--white);border:1px solid #d8d0e0;color:var(--purple);font-family:"Cabin",sans-serif;font-weight:700;font-size:10px;display:flex;align-items:center;justify-content:center}
.slide-dots span.on{background:var(--purple);color:var(--white);border-color:var(--purple)}
.rule{height:1px;background:var(--rule)}
.vrule{width:1px;background:var(--rule)}
h2{font-family:"Cabin",sans-serif;font-weight:500;color:var(--purple);font-size:20.5px;position:absolute;white-space:nowrap}
.copy{position:absolute;line-height:16.9px;text-align:justify}
.copy p+p{margin-top:16.9px}
.test-btn{left:459px;top:687px;width:182px;height:32px;background:var(--indigo);border:1px solid #4b4bb0;display:flex;align-items:center;color:var(--white);font-family:"Cabin",sans-serif;font-weight:700;font-size:16.5px;letter-spacing:.3px}
.test-btn svg{margin:0 15px 0 10px}
.field{width:260px;height:30px;background:linear-gradient(#e9e9e9,#f6f6f6);border:1px solid #d6d6d6;font-size:11.5px;color:#8a8a8a;padding:9px 15px;letter-spacing:.3px}
.submit-btn{left:770px;top:688px;width:92px;height:30px;background:var(--indigo);border:1px solid var(--indigo-dark);color:var(--white);font-family:"Cabin",sans-serif;font-weight:600;font-size:14px;display:flex;align-items:center;justify-content:center}
.date-tag{width:84px;height:25px;background:var(--purple);color:var(--white);font-family:"Cabin",sans-serif;font-weight:600;font-size:12px;display:flex;align-items:center;justify-content:center}
.news-title{position:absolute;color:var(--indigo);font-size:11.3px;white-space:nowrap}
.social{left:154px;top:962px;display:flex}
.social span{width:22px;height:22px;border-radius:3px;margin-right:8px}
.footer-text{position:absolute;line-height:17px;font-size:11.3px;white-space:nowrap}
.footer-text a{color:var(--indigo);text-decoration:none}
</style>
</head>
<body>
<div class="abs top-strip"></div>
<header class="abs site-header"></header>
<div class="abs brand">
  <span class="brand-mark"></span>
  <span class="brand-name">THE<span class="big">SKYVALE</span>PERSONAL DEVELOPMENT<br>CENTER</span>
</div>
<nav class="abs main-nav">
  <a class="active" style="left:513px">HOME</a>
  <a style="left:586px">ABOUT</a>
  <a style="left:668px">SERVICES</a>
  <a style="left:757px">TRAINERS</a>
  <a style="left:835px">BLOG</a>
  <a style="left:913px">GALLERY</a>
  <a style="left:1001px">CONTACT</a>
</nav>
<div class="abs nav-pointer"></div>
<div class="abs nav-underline"></div>

<div class="abs hero-band"></div>
<div class="abs slider-shadow"></div>
<div class="abs slider-frame"></div>
<div class="abs slide" role="img" aria-label="Photo of a trainer coaching three people working at computers in an office"></div>
<div class="abs slide-dots"><span class="on">1</span><span>2</span><span>3</span><span>4</span></div>

<div class="abs rule" style="left:150px;top:534px;width:900px"></div>

<h2 style="left:151px;top:556px">Welcome!</h2>
<div class="copy" style="left:150px;top:600px;width:281px">
  <p>ed ut perspiciatis unde omnis iste natus error sit voluptatem accusantium doloremque laudantium,</p>
  <p>totam rem aperiam, eaque ipsa quae ab illo inventore veritatis et quasi architecto beatae vitae dicta sunt expli-cabo. Nemo enim ipsam voluptatem quia voluptas sit aspernatur aut odit aut fugit,</p>
</div>
<div class="abs vrule" style="left:444px;top:563px;height:185px"></div>

<h2 style="left:461px;top:556px">Personality Test</h2>
<div class="copy" style="left:460px;top:600px;width:282px">
  <p>totam rem aperiam, eaque ipsa quae ab illo inventore veritatis et quasi architecto beatae vitae dicta sunt expli-cabo. Nemo enim ipsam voluptatem quia voluptas sit aspernatur aut odit aut fugit,</p>
</div>
<div class="abs test-btn">
  <svg width="28" height="20" viewBox="0 0 28 20" aria-hidden="true"><rect x="1" y="1" width="26" height="18" fill="none" stroke="#fff" stroke-width="2"/><rect x="4" y="4" width="20" height="10" fill="#fff"/><path d="M6 12 L12 8 L15 10 L22 5" stroke="#2d2d8c" stroke-width="2" fill="none"/></svg>
  TAKE THE TEST
</div>
<div class="abs vrule" style="left:757px;top:563px;height:185px"></div>

<h2 style="left:772px;top:556px">Newsletter Signup</h2>
<div class="abs field" style="left:770px;top:604px">Enter&nbsp; Name</div>
<div class="abs field" style="left:770px;top:645px">Enter&nbsp; Your Email</div>
<div class="abs submit-btn">SUBMIT</div>

<div class="abs rule" style="left:150px;top:762px;width:900px"></div>
<h2 style="left:151px;top:769px">Latest News</h2>
<div class="abs rule" style="left:150px;top:804px;width:900px"></div>

<div class="abs date-tag" style="left:153px;top:829px">16 FEB 2013</div>
<div class="news-title" style="left:153px;top:869px">ed ut perspiciatis unde omnis iste natus error sit</div>
<div class="copy" style="left:153px;top:890px;width:284px">ed ut perspiciatis unde omnis iste natus error sit voluptatem accusantium doloremque laudantium,</div>

<div class="abs date-tag" style="left:460px;top:829px">16 FEB 2013</div>
<div class="news-title" style="left:460px;top:869px">ed ut perspiciatis unde omnis iste natus error sit</div>
<div class="copy" style="left:460px;top:890px;width:284px">ed ut perspiciatis unde omnis iste natus error sit voluptatem accusantium doloremque laudantium,</div>

<div class="abs date-tag" style="left:770px;top:829px">16 FEB 2013</div>
<div class="news-title" style="left:770px;top:869px">ed ut perspiciatis unde omnis iste natus error sit</div>
<div class="copy" style="left:770px;top:890px;width:283px">ed ut perspiciatis unde omnis iste natus error sit voluptatem accusantium doloremque laudantium,</div>

<div class="abs rule" style="left:150px;top:947px;width:900px"></div>

<footer>
  <div class="abs social">
    <span style="background:#3b5998"></span>
    <span style="background:#5fb8e6"></span>
    <span style="background:#1f6fa8"></span>
    <span style="background:#f0701c"></span>
  </div>
  <div class="footer-text" style="left:153px;top:1003px">Copyright © 2013. Skyvale. All Rights Reserved.</div>
  <div class="footer-text" style="left:707px;top:964px">Skyvale Learning Ltd.<br>4127 Larkfield Lane,<br>Brookhaven, BH7 2QT.</div>
  <div class="footer-text" style="left:894px;top:964px">Freephone:&nbsp;&nbsp; +1 800 555 0142<br>FAX:&nbsp; +1 504 555 0187<br><a>E-mail: hello@skyvale-example.org</a></div>
</footer>
</body>
</html>
```